Veltro Metrics New Website for Health Benefits Plan Decisioneering Tool Launch

Veltro Metrics is a SaaS provider of health benefits comparison tools. We need a new simple SaaS focused website to direct customers to our product

Target Market(s)

General Public comparing their health benefits plans from their employer or from the state exchanges in the US

Coding

Coded - Design and coding required

Number of Pages Required

3 page

Requirements
Must have
• Main page - "Know the Best Health Benefits Plan for You!"
Graphic of a person looking over papers on their desk
Compare Now button to link to SaaS product
About Us
Product Page

https://plimquo.example/top-saas-sites/

```html
<!DOCTYPE html>
<html lang="en">
<head>
<meta charset="utf-8">
<title>Veltro Metrics — Know the Best Health Benefits Plan for You</title>
<link href="https://fonts.googleapis.com/css2?family=Raleway:wght@400;500;600;700&family=Montserrat:wght@400;500;600&display=swap" rel="stylesheet">
<style>
  :root{
    --page-bg:#e7eaee;
    --hero-bg:#e2e6ec;
    --ink:#16181c;
    --muted:#5f6670;
    --brand:#3fa2d6;
    --accent:#f2a257;
    --accent-ink:#2a2116;
    --tile:#b9d6ea;
    --frame:#0f1012;
    --dots:#9aa1aa;
    --footer-bg:#3a3e47;
    --footer-ink:#e6e8ec;
    --footer-muted:#b8bdc5;
    --field-line:#9aa1ab;
    --send-bg:#2c4f68;
    --send-ink:#7cc0e6;
  }
  *{box-sizing:border-box;margin:0;padding:0}
  html,body{width:1200px;height:3152px;overflow:hidden}
  body{position:relative;background:var(--page-bg);font-family:"Raleway",sans-serif;color:var(--ink)}
  .abs{position:absolute}

  /* header */
  .site-header{left:0;top:0;width:1200px;height:150px;background:var(--page-bg)}
  .brand{left:40px;top:40px;width:420px;text-align:center;color:var(--brand);font-family:"Raleway",sans-serif;font-weight:500}
  .brand-name{font-size:40px;letter-spacing:2px;line-height:44px;text-transform:uppercase}
  .brand-sub{font-size:20px;letter-spacing:4px;line-height:24px}
  .nav{top:42px;font-family:"Montserrat",sans-serif;font-size:24px;color:var(--ink)}
  .nav-home{left:580px;padding-bottom:14px;border-bottom:3px solid var(--brand)}
  .nav-about{left:752px}
  .nav-products{left:948px}

  /* hero */
  .hero{left:0;top:150px;width:1200px;height:810px;background:var(--hero-bg)}
  .hero-title{left:120px;top:270px;font-size:56px;line-height:64px;font-weight:700;text-transform:uppercase;letter-spacing:0.5px}
  .cta{left:120px;top:576px;width:272px;height:64px;background:var(--accent);color:var(--accent-ink);
       font-family:"Montserrat",sans-serif;font-weight:600;font-size:20px;letter-spacing:1px;
       display:flex;align-items:center;justify-content:center;gap:18px;text-decoration:none}
  .tile{background:var(--tile)}
  .hero-photo{left:620px;top:208px;width:460px;height:688px;background:linear-gradient(160deg,#b8c6d6 0%,#e8e1d6 45%,#d2b894 100%)}
  .scroll-dot{left:586px;top:850px}

  .photo{border:none}
  .copy{font-size:30px;line-height:36px;font-weight:500}
  .frame{background:var(--frame)}
  .dotline{width:0;border-left:4px dotted var(--dots)}

  /* footer */
  .site-footer{left:0;top:2488px;width:1200px;height:664px;background:var(--footer-bg);color:var(--footer-ink);font-family:"Montserrat",sans-serif}
  .footer-title{left:0;top:2522px;width:1200px;text-align:center;font-size:28px;letter-spacing:1px;color:var(--footer-ink)}
  .contact{right:660px;text-align:right}
  .contact-label{font-size:24px;letter-spacing:1px;color:var(--footer-ink)}
  .contact-value{font-size:18px;color:var(--footer-muted)}
  .divider{left:600px;top:2596px;height:500px;border-left:2px dashed #6d737d}
  .field{border:2px solid var(--field-line);color:var(--footer-muted);font-size:18px;padding:6px 12px}
  .send{left:648px;top:2948px;width:220px;height:36px;background:var(--send-bg);color:var(--send-ink);font-size:16px;letter-spacing:1px;display:flex;align-items:center;justify-content:center}
  .social{top:3022px;display:flex;gap:28px;right:660px}
  .social span{width:22px;height:22px;border-radius:50%;background:var(--footer-ink)}
  .copyright{left:0;top:3120px;width:1200px;text-align:center;font-size:14px;color:var(--footer-muted)}
</style>
</head>
<body>

<header class="abs site-header">
  <div class="abs brand">
    <div class="brand-name">Veltro Metrics</div>
    <div class="brand-sub">LLC</div>
  </div>
  <nav>
    <a class="abs nav nav-home">Home</a>
    <a class="abs nav nav-about">About Us</a>
    <a class="abs nav nav-products">Products</a>
  </nav>
</header>

<section class="abs hero"></section>
<h1 class="abs hero-title">Know the best<br>health benefits<br>plan for you!</h1>
<a class="abs cta" href="#compare">COMPARE NOW
  <svg width="40" height="24" viewBox="0 0 40 24" fill="none" stroke="#2a2116" stroke-width="3"><path d="M2 12h30M24 4l8 8-8 8M36 2v20"/></svg>
</a>
<div class="abs tile" style="left:520px;top:608px;width:44px;height:44px"></div>
<div class="abs tile" style="left:564px;top:652px;width:44px;height:44px;opacity:.7"></div>
<div class="abs tile" style="left:592px;top:590px;width:32px;height:32px;opacity:.6"></div>
<div class="abs hero-photo" role="img" aria-label="Person reviewing papers at a desk with a laptop and stationery"></div>
<svg class="abs scroll-dot" width="28" height="28" viewBox="0 0 28 28"><circle cx="14" cy="14" r="11" fill="none" stroke="#16181c" stroke-width="2.5"/><path d="M9 12l5 5 5-5" fill="none" stroke="#16181c" stroke-width="2.5"/></svg>
<div class="abs dotline" style="left:72px;top:720px;height:600px"></div>

<!-- feature 1 -->
<div class="abs photo" style="left:108px;top:928px;width:572px;height:376px;background:linear-gradient(180deg,#f2f3f4 0%,#d9dcdf 60%,#3a3d42 100%)" role="img" aria-label="Bright modern office lounge with plants and chairs"></div>
<div class="abs frame" style="left:640px;top:928px;width:40px;height:40px"></div>
<div class="abs frame" style="left:664px;top:928px;width:16px;height:376px;opacity:0"></div>
<p class="abs copy" style="left:712px;top:940px">Lorem ipsum dolor sit<br>amet, consectetuer ad-<br>ipiscing elit, sed diam<br>nonummy nibh euis-</p>

<!-- feature 2 -->
<div class="abs dotline" style="left:1140px;top:1380px;height:460px"></div>
<p class="abs copy" style="left:140px;top:1488px;text-align:right;width:340px">Lorem ipsum dolor sit<br>amet, consectetuer ad-<br>ipiscing elit, sed diam<br>nonummy nibh euis-</p>
<div class="abs frame" style="left:496px;top:1460px;width:28px;height:400px"></div>
<div class="abs photo" style="left:524px;top:1460px;width:564px;height:400px;background:linear-gradient(135deg,#2f7a3a 0%,#d9dbe2 40%,#2a58b8 75%,#1b2230 100%)" role="img" aria-label="Clinician in gloves treating a patient"></div>

<!-- feature 3 -->
<div class="abs dotline" style="left:80px;top:1960px;height:440px"></div>
<div class="abs photo" style="left:112px;top:2088px;width:548px;height:368px;background:linear-gradient(120deg,#e9e4df 0%,#c99a7e 40%,#2f5a48 65%,#3aa39a 100%)" role="img" aria-label="Therapist guiding a patient through a stretching exercise"></div>
<div class="abs frame" style="left:636px;top:2088px;width:28px;height:368px"></div>
<p class="abs copy" style="left:672px;top:2192px">Lorem ipsum dolor sit<br>amet, consectetuer ad-<br>ipiscing elit, sed diam<br>nonummy nibh euis-</p>

<!-- footer -->
<footer class="abs site-footer"></footer>
<h2 class="abs footer-title" style="font-weight:500">GET IN TOUCH</h2>

<div class="abs contact" style="top:2604px">
  <div class="contact-label">EMAIL</div>
  <div class="contact-value" style="margin-top:14px">hello@veltrometrics.example</div>
</div>
<div class="abs contact" style="top:2730px">
  <div class="contact-label">PHONE</div>
  <div class="contact-value" style="margin-top:14px">+1 (000) 555-0142</div>
</div>
<div class="abs contact" style="top:2852px">
  <div class="contact-label">ADDRESS</div>
  <div class="contact-value" style="margin-top:14px">48 Larkspur Lane, Springfield, ST 00000</div>
</div>
<div class="abs contact" style="top:2974px">
  <div class="contact-label">SOCIAL MEDIA</div>
</div>
<div class="abs social"><span></span><span></span><span></span></div>

<div class="abs divider"></div>

<div class="abs field" style="left:648px;top:2672px;width:220px;height:40px">Name</div>
<div class="abs field" style="left:928px;top:2672px;width:224px;height:40px">Email</div>
<div class="abs field" style="left:648px;top:2768px;width:504px;height:128px">Message</div>
<div class="abs send">SEND MESSAGE</div>

<div class="abs copyright">© Veltro Metrics 2020</div>

</body>
</html>
```